Time for a new business card design

We need a new business card design for Tolvik Furniture Rentals based in Australia. www.tolvik-example.com.au. We specialise in providing furniture rentals for home staging, corporate relocations events and product launches etc. We would like to see designs that include our logo on the front of the card with all the standard contact details as well as having a realy nice image on the back with a list of our services we offer. Our logo is red and this cannot change. Were looking for a pallet of red and white with maybe a splash of grey. The final design should communication organised & stylish. We are in the process of finalising our new website and would like the card design to compliment this as well

Requirements
Must have
• Square corners
logo
name, title, email, phone, address
image on back of card with space for list of services we offer
Services:
•Furniture and appliance rental
•Property styling
•Events and functions
•Office furniture rental

The card must be landscape.
The image is to appear on the back of the card only.

```html
<!DOCTYPE html>
<html lang="en">
<head>
<meta charset="utf-8">
<title>Tolvik Furniture Rentals – Business Card</title>
<link rel="stylesheet" href="https://fonts.googleapis.com/css2?family=Lato:wght@400;700&family=Tenor+Sans&display=swap">
<style>
  :root {
    --red: #c8141f;
    --red-bright: #e01b24;
    --red-deep: #a80f18;
    --white: #ffffff;
    --paper: #f4f4f4;
    --grey-text: #3a3a3a;
    --stage: #ececec;
    --night: #1d2a3a;
    --accent: #f2a31b;
  }
  * { margin: 0; padding: 0; box-sizing: border-box; }
  html, body { width: 1200px; height: 521px; overflow: hidden; }
  body { background: var(--stage); font-family: "Lato", Arial, sans-serif; position: relative; }

  .card { position: absolute; top: 113px; width: 522px; height: 297px; overflow: hidden; }
  .card--front { left: 60px; background: linear-gradient(180deg, var(--white) 30%, #ececec 70%, #e2e2e2 100%); }
  .card--back { left: 613px; }

  .front__header {
    position: absolute; left: 0; top: 0; width: 100%; height: 100px;
    background: linear-gradient(90deg, var(--red-bright) 0%, var(--red) 55%, var(--red-deep) 100%);
  }
  .front__footer { position: absolute; left: 0; bottom: 0; width: 100%; height: 12px; background: var(--red); }

  .wordmark { position: absolute; color: var(--white); font-family: "Lato", Arial, sans-serif; font-weight: 400; white-space: nowrap; }
  .front__header .wordmark { left: 30px; top: 28px; font-size: 38px; letter-spacing: -0.5px; }
  .wordmark small { font-size: 0.5em; }

  .contacts { position: absolute; left: 30px; top: 150px; list-style: none; }
  .contacts li { display: flex; align-items: center; height: 34px; font-size: 13px; color: var(--grey-text); }
  .contacts svg { width: 14px; height: 14px; margin-right: 13px; flex: none; }

  .person { position: absolute; right: 30px; top: 162px; text-align: right; }
  .person__name { font-family: "Tenor Sans", Georgia, serif; font-weight: 400; font-size: 30px; color: var(--red); line-height: 1; }
  .person__title { font-size: 13px; color: var(--grey-text); margin-top: 12px; }

  .back__photo {
    position: absolute; left: 0; top: 0; width: 314px; height: 297px;
    background:
      linear-gradient(180deg, #3d7fc4 0%, #9cc4e6 22%, #2b3340 23%, #5a606a 38%, #dfe3e8 55%, #c9ced6 78%, #8b929c 100%);
  }
  .back__panel {
    position: absolute; left: 314px; top: 0; width: 208px; height: 297px;
    background: linear-gradient(180deg, var(--night) 0%, #2f4a66 55%, #4f6b86 100%);
  }
  .back__panel svg.panel-shape { position: absolute; left: 0; top: 0; width: 208px; height: 297px; }
  .services { position: absolute; left: 13px; top: 14px; color: var(--white); }
  .services h2 { font-family: "Lato", Arial, sans-serif; font-weight: 400; font-size: 15px; letter-spacing: 0.5px; margin-bottom: 9px; }
  .services ul { list-style: none; }
  .services li { font-weight: 700; font-size: 11.5px; height: 26.5px; display: flex; align-items: center; }
  .services li::before { content: "»"; color: var(--accent); font-weight: 700; margin-right: 7px; font-size: 13px; }
  .back__panel .wordmark { left: 30px; bottom: 18px; font-size: 28px; letter-spacing: -0.5px; }
</style>
</head>
<body>

<section class="card card--front">
  <header class="front__header">
    <div class="wordmark">tolvik <small>furniture rentals</small></div>
  </header>

  <ul class="contacts">
    <li>
      <svg viewBox="0 0 14 14"><rect x="1" y="3" width="12" height="9" fill="var(--red)"/><path d="M1 3 L7 8 L13 3" stroke="#fff" stroke-width="1.2" fill="none"/></svg>
      marcus.hale@tolvik-example.com.au
    </li>
    <li>
      <svg viewBox="0 0 14 14"><path d="M3 1 L5.5 1 L6.5 4.5 L5 5.8 Q6.5 8.5 8.2 9 L9.5 7.5 L13 8.5 L13 11 Q12.5 13 10.5 13 Q1 11.5 1 3 Q1 1 3 1 Z" fill="var(--red)"/></svg>
      1800 55 01 99
    </li>
    <li>
      <svg viewBox="0 0 14 14" fill="none" stroke="var(--red)" stroke-width="1.2"><circle cx="7" cy="7" r="5.6"/><ellipse cx="7" cy="7" rx="2.4" ry="5.6"/><path d="M1.4 7 H12.6 M2.5 4 H11.5 M2.5 10 H11.5"/></svg>
      www.tolvik-example.com.au
    </li>
  </ul>

  <div class="person">
    <h1 class="person__name">Marcus Hale</h1>
    <p class="person__title">Managing Director</p>
  </div>

  <div class="front__footer"></div>
</section>

<section class="card card--back">
  <div class="back__photo" role="img" aria-label="Photo of a styled daybed with white linen and patterned cushions beside a bright window"></div>
  <div class="back__panel">
    <svg class="panel-shape" viewBox="0 0 208 297" aria-hidden="true">
      <polygon points="0,148 104,212 208,148 208,297 0,297" fill="var(--white)"/>
      <polygon points="0,158 104,222 208,158 208,297 0,297" fill="var(--red)"/>
    </svg>
    <div class="services">
      <h2>OUR SERVICES</h2>
      <ul>
        <li>Furniture and appliance rental</li>
        <li>Property styling</li>
        <li>Events and functions</li>
        <li>Office furniture rental</li>
      </ul>
    </div>
    <div class="wordmark">tolvik <small>furniture rentals</small></div>
  </div>
</section>

</body>
</html>
```